Canvasline Registry, LLC needs clean, modern business card design

Canvasline Registry is based in Honolulu. We offer fine arts collections management and documentation services for private and corporate art collectors. I would like to use my logo (attached). Card can be either single or double sided and either vertical or horizontal. My clients are businesses with art collections (banks, law firms, etc.) and wealthy individual collectors.

```html
<!DOCTYPE html>
<html lang="en">
<head>
<meta charset="utf-8">
<title>Canvasline Registry – Business Card</title>
<link href="https://fonts.googleapis.com/css2?family=Cabin+Condensed:wght@400;500;600;700&display=swap" rel="stylesheet">
<style>
  :root {
    --page-bg: #e6e3de;
    --card-light: #f3f3f2;
    --card-mid: #e2e3e4;
    --charcoal: #3b3d40;
    --charcoal-deep: #2e3033;
    --accent-blue: #35a3d3;
    --accent-teal: #1f8294;
    --text-dark: #3a3a3c;
    --text-black: #141414;
    --silver: #cfd2d4;
  }
  * { box-sizing: border-box; margin: 0; padding: 0; }
  html, body {
    width: 1200px;
    height: 970px;
    overflow: hidden;
    background: var(--page-bg);
    font-family: "Cabin Condensed", "Arial Narrow", sans-serif;
  }
  .business-card {
    position: absolute;
    left: 60px;
    top: 185px;
    width: 1080px;
    height: 600px;
    box-shadow: 0 10px 30px rgba(0,0,0,0.18);
    overflow: hidden;
  }
  .card-shapes {
    position: absolute;
    inset: 0;
    width: 100%;
    height: 100%;
  }
  .brand {
    position: absolute;
    left: 55px;
    top: 150px;
    display: flex;
    align-items: center;
    gap: 22px;
  }
  .brand-name {
    font-size: 60px;
    font-weight: 600;
    color: var(--text-dark);
    line-height: 1;
  }
  .brand-mark {
    width: 78px;
    height: 78px;
    border-radius: 50%;
    border: 5px solid var(--accent-blue);
  }
  .tagline {
    position: absolute;
    left: 52px;
    top: 340px;
    font-size: 24px;
    font-weight: 600;
    color: var(--accent-blue);
  }
  .contact-list {
    position: absolute;
    left: 52px;
    top: 412px;
    list-style: none;
  }
  .contact-item {
    display: flex;
    align-items: center;
    height: 34px;
    font-size: 23px;
    color: var(--text-dark);
  }
  .contact-item.phone { font-size: 26px; }
  .contact-icon {
    width: 18px;
    height: 18px;
    margin-right: 18px;
    fill: var(--text-dark);
    flex: none;
  }
  .person {
    position: absolute;
    right: 50px;
    top: 470px;
    text-align: center;
  }
  .person-name {
    font-size: 48px;
    font-weight: 600;
    color: var(--accent-teal);
    line-height: 1;
  }
  .person-role {
    font-size: 19px;
    font-weight: 700;
    color: var(--text-black);
    margin-top: 4px;
  }
</style>
</head>
<body>
  <article class="business-card">
    <svg class="card-shapes" viewBox="0 0 1080 600" preserveAspectRatio="none" aria-hidden="true">
      <defs>
        <linearGradient id="card-surface" x1="0" y1="0" x2="1" y2="1">
          <stop offset="0" stop-color="var(--card-light)"/>
          <stop offset="1" stop-color="var(--card-mid)"/>
        </linearGradient>
        <linearGradient id="charcoal-fill" x1="0" y1="0" x2="1" y2="0">
          <stop offset="0" stop-color="var(--charcoal)"/>
          <stop offset="1" stop-color="var(--charcoal-deep)"/>
        </linearGradient>
      </defs>
      <rect class="surface" width="1080" height="600" fill="url(#card-surface)"/>
      <path class="silver-band" d="M0,92 C150,66 300,52 450,54 C700,60 950,190 1080,312 V340 C950,230 700,84 450,74 C300,70 150,82 0,100 Z" fill="var(--silver)"/>
      <path class="charcoal-band" d="M0,0 H1080 V305 C950,185 700,55 450,48 C300,45 150,58 0,84 Z" fill="url(#charcoal-fill)"/>
      <path class="blue-swoosh" d="M10,100 C150,76 300,62 450,64 C700,72 950,210 1080,330 V375 C950,262 700,98 450,80 C300,74 150,86 10,100 Z" fill="var(--accent-blue)"/>
    </svg>

    <div class="brand">
      <span class="brand-name">Canvasline Registry</span>
      <span class="brand-mark"></span>
    </div>

    <p class="tagline">"Fine Arts Collections Management Services"</p>

    <ul class="contact-list">
      <li class="contact-item phone">
        <svg class="contact-icon" viewBox="0 0 24 24"><path d="M6.6 10.8a15.2 15.2 0 0 0 6.6 6.6l2.2-2.2a1 1 0 0 1 1-.25 11.4 11.4 0 0 0 3.6.57 1 1 0 0 1 1 1V20a1 1 0 0 1-1 1A17 17 0 0 1 3 4a1 1 0 0 1 1-1h3.5a1 1 0 0 1 1 1c0 1.25.2 2.45.57 3.57a1 1 0 0 1-.25 1z"/></svg>
        (808) 555-0147
      </li>
      <li class="contact-item">
        <svg class="contact-icon" viewBox="0 0 24 24"><path d="M2 5h20v14H2z M2 5l10 8 10-8" fill="none" stroke="var(--text-dark)" stroke-width="2"/><path d="M2 5h20l-10 8z"/></svg>
        www.canvaslineregistry.com
      </li>
      <li class="contact-item">
        <svg class="contact-icon" viewBox="0 0 24 24"><circle cx="12" cy="12" r="10"/><path d="M6 8c2 0 3 2 5 2s1 3 3 3-1 4-2 6M14 4c0 2 2 2 3 4s3 1 4 2" fill="none" stroke="var(--card-light)" stroke-width="1.8"/></svg>
        hello@canvaslineregistry.com
      </li>
      <li class="contact-item">
        <svg class="contact-icon" viewBox="0 0 24 24"><path d="M12 2a7 7 0 0 0-7 7c0 5.2 7 13 7 13s7-7.8 7-13a7 7 0 0 0-7-7zm0 9.5A2.5 2.5 0 1 1 12 6.5a2.5 2.5 0 0 1 0 5z"/></svg>
        1420 Kapena Lane Honolulu, HI 96815
      </li>
    </ul>

    <div class="person">
      <p class="person-name">Leilani M. Foster</p>
      <p class="person-role">Owner/Manager</p>
    </div>
  </article>
</body>
</html>
```